Flyer for 3D CAD (computer aided drafting) company

We are 3D CAD designers, we would like an A4 flyer to hand out to potential customers, mainly use Formvanta software (check out formvanta.com). Can supply some pictures of our work but a lot of what we do is confidential so would prefer to use the flyer to show what we can do somehow without showing too many of our clients drawings. Also for software see plixaro.com
Use colors as supplied in logo
Check out https://www.stashbin.net/sh/k7qr2m9xw4zt1pd/BBqT8nW3vLx2HykmRcEeKjSpWa?dl=0 for some examples of our work

Target Market(s)

Manufacturing, engineering, maintenance

Industry/Entity Type

Computer

Requirements
Must have
• Logo (supplied)
• Phone(0472 581 436)
• Email (info@morvex.net)

```html
<!DOCTYPE html>
<html lang="en">
<head>
<meta charset="utf-8">
<title>Morvex – Professional 3D CAD Design</title>
<link href="https://fonts.googleapis.com/css2?family=Montserrat:wght@400;500;600;700;800&display=swap" rel="stylesheet">
<style>
  :root {
    --red: #e3262b;
    --navy: #1d2347;
    --white: #ffffff;
    --ink: #1d2347;
    --floor-light: #f1f3f6;
    --floor-mid: #d9dee5;
    --floor-blue: #b9c6d8;
  }
  * { margin: 0; padding: 0; box-sizing: border-box; }
  html, body { width: 849px; height: 1200px; overflow: hidden; background: var(--white); }
  body { font-family: "Montserrat", Arial, sans-serif; }

  .flyer { position: relative; width: 849px; height: 1200px; overflow: hidden; background: var(--white); }
  .backdrop, .hero-render { position: absolute; left: 0; top: 0; width: 849px; height: 1200px; }

  .brand { position: absolute; left: 40px; top: 28px; }
  .brand-name { font-size: 48px; font-weight: 800; color: var(--red); letter-spacing: 2px; line-height: 1; }
  .brand-tagline { margin-top: 6px; font-size: 17px; font-weight: 600; color: var(--ink); }

  .slogan {
    position: absolute; right: 40px; top: 30px; text-align: right;
    font-size: 28px; font-weight: 700; color: var(--ink); line-height: 1.2;
  }

  .intro { position: absolute; left: 48px; top: 668px; width: 730px; color: var(--white); }
  .intro-title { font-size: 31px; font-weight: 500; line-height: 1.2; }
  .intro-text { margin-top: 12px; font-size: 15.5px; line-height: 1.4; }
  .intro-text strong { font-weight: 700; }

  .work-gallery {
    position: absolute; left: 48px; top: 772px; width: 773px; height: 164px;
    display: flex; gap: 10px;
  }
  .work-sample { flex: 1; }
  .work-sample.trailer { background: radial-gradient(ellipse at 45% 55%, #aeb2b8 0%, #d4d6da 45%, #eceef0 100%); }
  .work-sample.racking { background: radial-gradient(ellipse at 50% 50%, #c3ccd8 0%, #dde3ea 50%, #f2f4f7 100%); }
  .work-sample.bench { background: radial-gradient(ellipse at 55% 55%, #d9cdbd 0%, #ebe5dc 50%, #f7f5f1 100%); }

  .outro {
    position: absolute; left: 48px; top: 946px; width: 700px;
    font-size: 15.5px; line-height: 1.38; color: var(--white);
  }

  .call-bar {
    position: absolute; left: 0; top: 1036px; width: 849px; height: 36px;
    background: var(--red); color: var(--white);
    font-size: 27px; font-weight: 700; text-align: center; line-height: 36px;
  }

  .contact { position: absolute; left: 0; top: 1074px; width: 849px; text-align: center; color: var(--red); }
  .contact-phone { font-size: 60px; font-weight: 700; letter-spacing: 1px; line-height: 1.1; }
  .contact-email { font-size: 28px; font-weight: 700; margin-top: 4px; }
</style>
</head>
<body>
<main class="flyer">
  <svg class="backdrop" viewBox="0 0 849 1200" aria-hidden="true">
    <polygon points="0,665 849,396 849,1036 0,1036" fill="var(--navy)"/>
    <polygon points="0,612 560,600 0,640" fill="var(--red)"/>
  </svg>

  <svg class="hero-render" viewBox="0 0 849 1200" role="img" aria-label="3D CAD render of a warehouse layout with storage racking, conveyors and forklifts">
    <defs>
      <linearGradient id="floorTone" x1="0" y1="0" x2="1" y2="1">
        <stop offset="0" stop-color="var(--floor-light)"/>
        <stop offset="0.55" stop-color="var(--floor-mid)"/>
        <stop offset="1" stop-color="var(--floor-blue)"/>
      </linearGradient>
    </defs>
    <polygon points="42,311 410,127 820,325 467,580" fill="url(#floorTone)"/>
  </svg>

  <header class="brand">
    <div class="brand-name">MORVEX</div>
    <div class="brand-tagline">Professional 3D CAD Design</div>
  </header>

  <p class="slogan">We Make Your<br>Great Ideas Happen.</p>

  <section class="intro">
    <h1 class="intro-title">Let us work on your 3D project</h1>
    <p class="intro-text">With experts in the industry’s popular software such as <strong>Formvanta</strong> and <strong>Plixaro</strong><br>in our team, we’ll make sure your great ideas will be perfectly executed</p>
  </section>

  <section class="work-gallery">
    <div class="work-sample trailer" role="img" aria-label="3D model of a car trailer"></div>
    <div class="work-sample racking" role="img" aria-label="3D model of a steel racking structure"></div>
    <div class="work-sample bench" role="img" aria-label="3D model of an upholstered bench seat"></div>
  </section>

  <p class="outro">Get powerful 3D design solution for rapid creation of parts, assemblies, and<br>2D drawings<br>Contact us for more example of our wide-ranging portfolio.</p>

  <div class="call-bar">CALL US NOW</div>

  <section class="contact">
    <div class="contact-phone">0472 581 436</div>
    <div class="contact-email">or email: info@morvex.net</div>
  </section>
</main>
</body>
</html>
```